Artificial Intelligence based service LanePilot.ai

Looking for a website for service designed for driving schools to deliver AI based solutions and features. File are to include various pages from contact to list of services to faqs, demos and more. we are looking for a website for AI based service for driving schools. services will include things like chat bots, voice agent, document processing and ai based marketing.

Target Market(s)

driving school owners and managers.

Industry/Entity Type

software and AI

Number of Pages Required

4 page

Font styles to use
Sans Serif

Requirements
Must have
• clean and easy to navigate pages. responsive. also delivery via FIGMA.

```html
<!DOCTYPE html>
<html lang="en">
<head>
<meta charset="utf-8">
<title>LanePilot.AI — Website Pages</title>
<link href="https://fonts.googleapis.com/css2?family=Inter:wght@400;500;600;700&family=Outfit:wght@500;600;700&display=swap" rel="stylesheet">
<style>
:root{
  --board:#adb0b9;
  --brand:#5b3fe0;
  --brand-dark:#4f46e5;
  --violet:#7c3aed;
  --ink:#1f2340;
  --text:#4b5060;
  --muted:#6b7080;
  --line:#ebecf0;
  --soft:#f7f8fa;
  --hero-a:#f1ecfd;
  --hero-b:#f9f7fe;
  --bubble:#f1f1f4;
  --bubble-me:#e4e1fb;
  --star:#f5b800;
  --footer:#111827;
  --footer-text:#9ca3af;
  --white:#ffffff;
}
*{margin:0;padding:0;box-sizing:border-box}
html,body{width:1200px;height:1200px;overflow:hidden;background:var(--board)}
body{font-family:'Inter',sans-serif;color:var(--ink)}
.board{position:absolute;left:0;top:0;width:1932px;height:1932px;transform:scale(0.621118);transform-origin:0 0;background:var(--board)}
.board-title{position:absolute;left:0;right:0;top:38px;text-align:center;font-family:'Inter',sans-serif;font-weight:700;font-size:92px;letter-spacing:-1px;color:var(--brand)}
.page{position:absolute;background:var(--white);overflow:hidden}
.page-sm{width:882px;height:387px}
.p-hero{left:55px;top:196px}
.p-why{left:995px;top:196px}
.p-how{left:55px;top:635px}
.p-cta{left:995px;top:635px}
.p-reviews{left:55px;top:1074px;width:1822px;height:800px}

/* navigation */
.nav{position:absolute;left:0;top:0;right:0;height:42px;border-bottom:1px solid var(--line);background:var(--white);z-index:2}
.brand{position:absolute;left:24px;top:14px;display:flex;align-items:center;gap:6px;font-weight:700;font-size:12px;color:var(--ink)}
.brand-dot{width:14px;height:14px;border-radius:50%;background:var(--brand)}
.nav-links{position:absolute;right:26px;top:12px;display:flex;align-items:center;gap:18px;font-size:9px;color:var(--text)}
.nav-btn{background:var(--brand-dark);color:var(--white);padding:0 11px;height:22px;line-height:22px;border-radius:3px;margin-left:0}

.h2{font-family:'Outfit',sans-serif;font-weight:600;font-size:21px;color:var(--ink);text-align:center}
.lead{font-size:11px;line-height:15.5px;color:var(--text);text-align:center}

/* hero */
.hero-bg{position:absolute;left:0;top:42px;width:100%;height:314px;background:linear-gradient(110deg,var(--hero-a),var(--hero-b))}
.hero-title{position:absolute;left:23px;top:104px;font-family:'Outfit',sans-serif;font-weight:600;font-size:28px;line-height:27px;color:var(--ink)}
.hero-title em{font-style:normal;color:var(--brand)}
.hero-sub{position:absolute;left:23px;top:173px;font-size:11px;color:var(--text)}
.hero-actions{position:absolute;left:23px;top:206px;display:flex;gap:9px}
.btn{height:28px;display:flex;align-items:center;justify-content:center;font-size:9px;font-weight:500;border-radius:3px}
.btn-primary{width:124px;background:var(--brand);color:var(--white)}
.btn-outline{width:112px;border:1px solid var(--brand);color:var(--brand);background:var(--white)}
.trust{position:absolute;left:24px;top:252px;display:flex;align-items:center;gap:8px;font-size:7.5px;color:var(--muted)}
.trust b{color:var(--ink)}
.avatars{display:flex}
.avatars span{width:16px;height:16px;border-radius:50%;border:1.5px solid var(--white);background:#e6e3fb;color:var(--brand);font-size:5px;display:flex;align-items:center;justify-content:center;margin-right:-3px}
.avatars span:nth-child(2){background:#f3e1fb;color:#a23fd6}
.avatars span:nth-child(3){background:#e0ebfb;color:#3f6fe0}

.chat{position:absolute;left:440px;top:65px;width:416px;height:246px;background:var(--white);border-radius:8px;box-shadow:0 6px 22px rgba(70,60,140,.14)}
.chat-head{position:absolute;left:14px;top:14px;display:flex;gap:8px;align-items:center}
.chat-ico{width:20px;height:20px;border-radius:50%;background:var(--brand);display:flex;align-items:center;justify-content:center}
.chat-name{font-size:8.5px;font-weight:600;line-height:11px}
.chat-name small{display:block;font-size:6px;font-weight:400;color:#22a35a}
.chat-more{position:absolute;right:16px;top:16px;font-size:10px;color:var(--muted);letter-spacing:1px}
.msg{position:absolute;font-size:7px;line-height:10.5px;padding:6px 7px;border-radius:3px;color:var(--ink)}
.msg-in{left:14px;width:310px;background:var(--bubble)}
.msg-out{left:91px;width:312px;background:var(--bubble-me)}
.chat-input{position:absolute;left:14px;top:209px;width:360px;height:22px;border:1px solid #dcdde3;border-radius:3px 0 0 3px;font-size:7.5px;color:#9a9caa;padding:6px 8px}
.chat-send{position:absolute;left:374px;top:209px;width:28px;height:22px;background:var(--brand);border-radius:0 3px 3px 0;display:flex;align-items:center;justify-content:center}

/* why */
.why-title{position:absolute;left:0;right:0;top:68px}
.why-lead{position:absolute;left:220px;right:220px;top:100px}
.feature{position:absolute;top:167px;width:195px;height:135px;border:1px solid var(--line);border-radius:6px;padding:14px 13px}
.icon-dot{width:30px;height:30px;border-radius:50%;background:var(--brand);display:flex;align-items:center;justify-content:center}
.feature h3{margin-top:14px;font-size:11px;font-weight:600}
.feature p{margin-top:7px;font-size:8.3px;line-height:13.5px;color:var(--text)}
.why-band{position:absolute;left:0;right:0;top:346px;bottom:0;background:var(--soft)}

/* how */
.how-bg{position:absolute;left:0;top:42px;right:0;bottom:0;background:var(--soft)}
.how-title{position:absolute;left:0;right:0;top:68px}
.how-lead{position:absolute;left:210px;right:210px;top:100px}
.step{position:absolute;top:168px;width:262px;margin-left:-131px;text-align:center}
.step-num{width:44px;height:44px;margin:0 auto;border-radius:50%;background:linear-gradient(135deg,var(--brand-dark),var(--violet));color:var(--white);font-weight:600;font-size:13px;line-height:44px}
.step-ico{width:28px;height:28px;margin:-12px auto 0;border-radius:50%;background:var(--white);box-shadow:0 1px 4px rgba(0,0,0,.12);display:flex;align-items:center;justify-content:center;position:relative}
.step h3{margin-top:21px;font-size:11px;font-weight:600}
.step p{margin-top:8px;font-size:8.3px;line-height:13.5px;color:var(--text)}
.how-band{position:absolute;left:0;right:0;top:355px;bottom:0;background:linear-gradient(90deg,var(--brand-dark),var(--violet))}

/* cta */
.cta-band{position:absolute;left:0;right:0;top:42px;height:206px;background:linear-gradient(100deg,var(--brand-dark),var(--violet))}
.cta-title{position:absolute;left:0;right:0;top:68px;color:var(--white);line-height:22px}
.cta-lead{position:absolute;left:0;right:0;top:126px;color:#ece9ff}
.cta-actions{position:absolute;left:0;right:0;top:160px;display:flex;justify-content:center;gap:10px}
.btn-white{width:133px;background:var(--white);color:var(--brand-dark)}
.btn-ghost{width:89px;border:1px solid var(--white);color:var(--white)}
.cta-note{position:absolute;left:0;right:0;top:202px;text-align:center;font-size:7px;color:#dcd6ff}
.trusted-title{position:absolute;left:0;right:0;top:290px}
.trusted-lead{position:absolute;left:250px;right:250px;top:322px}

/* reviews page */
.nav-lg{height:90px}
.nav-lg .brand{left:50px;top:30px;gap:14px;font-size:25px}
.nav-lg .brand-dot{width:30px;height:30px}
.nav-lg .nav-links{right:53px;top:23px;gap:37px;font-size:20px}
.nav-lg .nav-btn{height:46px;line-height:46px;padding:0 22px;border-radius:4px}
.review{position:absolute;top:105px;width:549px;height:275px;border:1px solid var(--line);border-radius:8px;box-shadow:0 2px 8px rgba(0,0,0,.04);padding:26px 28px}
.stars{display:flex;gap:3px}
.stars svg{width:20px;height:20px}
.review blockquote{margin-top:17px;font-size:19.5px;line-height:27.5px;color:var(--text)}
.author{margin-top:22px;display:flex;align-items:center;gap:15px}
.author-av{width:44px;height:44px;border-radius:50%;background:#e6e3fb;color:var(--brand);font-weight:600;font-size:18px;display:flex;align-items:center;justify-content:center}
.author-name{font-size:19px;font-weight:600;color:var(--ink);line-height:26px}
.author-role{font-size:17px;color:var(--muted);line-height:26px}
.footer{position:absolute;left:0;right:0;top:473px;bottom:0;background:var(--footer);color:var(--white)}
.footer .brand{left:50px;top:56px;gap:14px;font-size:25px;color:var(--white)}
.footer .brand-dot{width:30px;height:30px}
.footer-desc{position:absolute;left:47px;top:108px;width:410px;font-size:19px;line-height:28px;color:var(--footer-text)}
.socials{position:absolute;left:47px;top:183px;display:flex;gap:19px}
.socials span{width:22px;height:22px;background:var(--footer-text)}
.socials span:nth-child(2){border-radius:50%}
.socials span:nth-child(3){border-radius:50%}
.f-col{position:absolute;top:57px}
.f-col h4{font-size:20px;font-weight:600}
.f-col ul{list-style:none;margin-top:20px}
.f-col li{font-size:19px;color:var(--footer-text);height:37px}
.footer-rule{position:absolute;left:47px;right:53px;top:298px;height:1px;background:#263043}
</style>
</head>
<body>
<div class="board">
  <h1 class="board-title">LanePilot.AI</h1>

  <!-- Home hero -->
  <section class="page page-sm p-hero">
    <nav class="nav">
      <div class="brand"><span class="brand-dot"></span>LanePilot.AI</div>
      <div class="nav-links"><span>Features</span><span>How It Works</span><span>Pricing</span><span class="nav-btn">Contact Us</span></div>
    </nav>
    <div class="hero-bg"></div>
    <h2 class="hero-title">Boost Your Driving School<br>with a <em>24/7 Voice Agent</em></h2>
    <p class="hero-sub">Automate Calls. Answer Questions Instantly. Never Miss a Student Again.</p>
    <div class="hero-actions"><span class="btn btn-primary">Try Voice Agent Free</span><span class="btn btn-outline">See How It Works</span></div>
    <div class="trust"><div class="avatars"><span>JD</span><span>KM</span><span>TS</span></div><span>Trusted by <b>200+</b> driving schools</span></div>
    <div class="chat">
      <div class="chat-head">
        <div class="chat-ico"><svg width="10" height="10" viewBox="0 0 24 24" fill="none" stroke="#fff" stroke-width="2.5"><path d="M4 5h16v11H9l-5 4z"/></svg></div>
        <div class="chat-name">LanePilot.AI<small>Online</small></div>
      </div>
      <div class="chat-more">···</div>
      <div class="msg msg-in" style="top:50px">Hi! I'd like to book a driving lesson for next week.</div>
      <div class="msg msg-out" style="top:83px">I'd be happy to help you book a driving lesson! What day and time works best for you next week?</div>
      <div class="msg msg-in" style="top:126px">Tuesday afternoon, around 3 PM if possible.</div>
      <div class="msg msg-out" style="top:159px">Great! I have Tuesday at 3 PM available with instructor Emily. Would you like me to book that slot for you?</div>
      <div class="chat-input">Type your message...</div>
      <div class="chat-send"><svg width="10" height="10" viewBox="0 0 24 24" fill="none" stroke="#fff" stroke-width="2.5"><path d="M12 3 3 21h18z"/></svg></div>
    </div>
  </section>

  <!-- Benefits -->
  <section class="page page-sm p-why">
    <nav class="nav">
      <div class="brand"><span class="brand-dot"></span>LanePilot.AI</div>
      <div class="nav-links"><span>Features</span><span>How It Works</span><span>Pricing</span><span class="nav-btn">Contact Us</span></div>
    </nav>
    <h2 class="h2 why-title">Why Driving Schools Love Voice Agents</h2>
    <p class="lead why-lead">Our AI-powered voice agent handles the calls so your team can focus on what matters most - teaching great drivers.</p>
    <div class="feature" style="left:23px">
      <div class="icon-dot"><svg width="14" height="14" viewBox="0 0 24 24" fill="none" stroke="#fff" stroke-width="2"><path d="M5 3h4l2 5-3 2a11 11 0 0 0 6 6l2-3 5 2v4a2 2 0 0 1-2 2A17 17 0 0 1 3 5a2 2 0 0 1 2-2z"/></svg></div>
      <h3>Handles High Call Volume</h3>
      <p>Never miss another inquiry. Our AI handles unlimited calls simultaneously, even during peak seasons.</p>
    </div>
    <div class="feature" style="left:236px">
      <div class="icon-dot"><svg width="14" height="14" viewBox="0 0 24 24" fill="none" stroke="#fff" stroke-width="2"><circle cx="12" cy="12" r="9"/><path d="M12 7v5l3 2"/></svg></div>
      <h3>Available 24/7</h3>
      <p>Capture after-hours inquiries and book lessons while you sleep. Never miss a potential student again.</p>
    </div>
    <div class="feature" style="left:449px">
      <div class="icon-dot"><svg width="14" height="14" viewBox="0 0 24 24" fill="none" stroke="#fff" stroke-width="2"><circle cx="9" cy="8" r="3"/><circle cx="16" cy="9" r="2.5"/><path d="M3 19c0-3 3-5 6-5s6 2 6 5M14 14c3 0 6 1.5 6 4"/></svg></div>
      <h3>Reduces Staff Workload</h3>
      <p>Free up your staff from repetitive phone tasks so they can focus on delivering quality instruction.</p>
    </div>
    <div class="feature" style="left:662px">
      <div class="icon-dot"><svg width="14" height="14" viewBox="0 0 24 24" fill="none" stroke="#fff" stroke-width="2"><rect x="4" y="5" width="16" height="15" rx="2"/><path d="M4 10h16M9 3v4M15 3v4"/></svg></div>
      <h3>Manages Instructor Absences</h3>
      <p>Automatically reschedule lessons when instructors are unavailable, keeping your schedule running smoothly.</p>
    </div>
    <div class="why-band"></div>
  </section>

  <!-- How it works -->
  <section class="page page-sm p-how">
    <nav class="nav">
      <div class="brand"><span class="brand-dot"></span>LanePilot.AI</div>
      <div class="nav-links"><span>Features</span><span>How It Works</span><span>Pricing</span><span class="nav-btn">Contact Us</span></div>
    </nav>
    <div class="how-bg"></div>
    <h2 class="h2 how-title">How the Voice Agent Works</h2>
    <p class="lead how-lead">Our AI voice agent integrates seamlessly with your existing systems to provide a frictionless experience.</p>
    <div class="step" style="left:162px">
      <div class="step-num">1</div>
      <div class="step-ico"><svg width="14" height="14" viewBox="0 0 24 24" fill="none" stroke="#5b3fe0" stroke-width="2"><circle cx="12" cy="12" r="9"/><path d="M9.5 9.5a2.5 2.5 0 1 1 3.5 2.3c-.7.3-1 .9-1 1.7M12 17h.01"/></svg></div>
      <h3>Answers FAQs Automatically</h3>
      <p>The AI voice agent answers common questions about pricing, lesson duration, requirements, and more without human intervention.</p>
    </div>
    <div class="step" style="left:440px">
      <div class="step-num">2</div>
      <div class="step-ico"><svg width="14" height="14" viewBox="0 0 24 24" fill="none" stroke="#5b3fe0" stroke-width="2"><rect x="4" y="5" width="16" height="15" rx="2"/><path d="M4 10h16M9 3v4M15 3v4"/></svg></div>
      <h3>Books Driving Lessons</h3>
      <p>Checks instructor availability in real-time and schedules lessons directly into your calendar system with student details.</p>
    </div>
    <div class="step" style="left:717px">
      <div class="step-num">3</div>
      <div class="step-ico"><svg width="14" height="14" viewBox="0 0 24 24" fill="none" stroke="#5b3fe0" stroke-width="2"><path d="M6 16V11a6 6 0 0 1 12 0v5l2 2H4zM10 21h4"/></svg></div>
      <h3>Sends Reminders &amp; Handles Reschedules</h3>
      <p>Automatically sends confirmation and reminder messages, and handles rescheduling requests with ease.</p>
    </div>
    <div class="how-band"></div>
  </section>

  <!-- Call to action -->
  <section class="page page-sm p-cta">
    <nav class="nav">
      <div class="brand"><span class="brand-dot"></span>LanePilot.AI</div>
      <div class="nav-links"><span>Features</span><span>How It Works</span><span>Pricing</span><span class="nav-btn">Contact Us</span></div>
    </nav>
    <div class="cta-band"></div>
    <h2 class="h2 cta-title">Ready to Transform Your Driving<br>School?</h2>
    <p class="lead cta-lead">No setup cost. No commitment. Start today.</p>
    <div class="cta-actions"><span class="btn btn-white">Book a Free Demo Now</span><span class="btn btn-ghost">View Pricing</span></div>
    <p class="cta-note">Join 200+ driving schools already using LanePilot.AI</p>
    <h2 class="h2 trusted-title">Trusted by Driving Schools Nationwide</h2>
    <p class="lead trusted-lead">See what our customers have to say about their experience with LanePilot.AI</p>
  </section>

  <!-- Testimonials and footer -->
  <section class="page p-reviews">
    <nav class="nav nav-lg">
      <div class="brand"><span class="brand-dot"></span>LanePilot.AI</div>
      <div class="nav-links"><span>Features</span><span>How It Works</span><span>Pricing</span><span class="nav-btn">Contact Us</span></div>
    </nav>
    <article class="review" style="left:47px">
      <div class="stars"><svg viewBox="0 0 24 24"><path fill="#f5b800" d="m12 2 3 7 7 .6-5.3 4.7L18.3 22 12 18l-6.3 4 1.6-7.7L2 9.6 9 9z"/></svg><svg viewBox="0 0 24 24"><path fill="#f5b800" d="m12 2 3 7 7 .6-5.3 4.7L18.3 22 12 18l-6.3 4 1.6-7.7L2 9.6 9 9z"/></svg><svg viewBox="0 0 24 24"><path fill="#f5b800" d="m12 2 3 7 7 .6-5.3 4.7L18.3 22 12 18l-6.3 4 1.6-7.7L2 9.6 9 9z"/></svg><svg viewBox="0 0 24 24"><path fill="#f5b800" d="m12 2 3 7 7 .6-5.3 4.7L18.3 22 12 18l-6.3 4 1.6-7.7L2 9.6 9 9z"/></svg><svg viewBox="0 0 24 24"><path fill="#f5b800" d="m12 2 3 7 7 .6-5.3 4.7L18.3 22 12 18l-6.3 4 1.6-7.7L2 9.6 9 9z"/></svg></div>
      <blockquote>"Since implementing LanePilot.AI, we've increased our bookings by 35% and reduced our administrative workload significantly. The voice agent handles all our after-hours calls perfectly."</blockquote>
      <div class="author"><div class="author-av">ME</div><div><div class="author-name">Mark Ellison</div><div class="author-role">Owner, Swiftline Driving Academy</div></div></div>
    </article>
    <article class="review" style="left:633px">
      <div class="stars"><svg viewBox="0 0 24 24"><path fill="#f5b800" d="m12 2 3 7 7 .6-5.3 4.7L18.3 22 12 18l-6.3 4 1.6-7.7L2 9.6 9 9z"/></svg><svg viewBox="0 0 24 24"><path fill="#f5b800" d="m12 2 3 7 7 .6-5.3 4.7L18.3 22 12 18l-6.3 4 1.6-7.7L2 9.6 9 9z"/></svg><svg viewBox="0 0 24 24"><path fill="#f5b800" d="m12 2 3 7 7 .6-5.3 4.7L18.3 22 12 18l-6.3 4 1.6-7.7L2 9.6 9 9z"/></svg><svg viewBox="0 0 24 24"><path fill="#f5b800" d="m12 2 3 7 7 .6-5.3 4.7L18.3 22 12 18l-6.3 4 1.6-7.7L2 9.6 9 9z"/></svg><svg viewBox="0 0 24 24"><path fill="#f5b800" d="m12 2 3 7 7 .6-5.3 4.7L18.3 22 12 18l-6.3 4 1.6-7.7L2 9.6 9 9z"/></svg></div>
      <blockquote>"The AI voice agent has been a game-changer for our driving school. It handles scheduling conflicts and student inquiries with incredible accuracy. Worth every penny!"</blockquote>
      <div class="author"><div class="author-av" style="background:#f6e2fa;color:#b23fd6">DW</div><div><div class="author-name">Dana Whitfield</div><div class="author-role">Manager, Keystone Driving School</div></div></div>
    </article>
    <article class="review" style="left:1220px">
      <div class="stars"><svg viewBox="0 0 24 24"><path fill="#f5b800" d="m12 2 3 7 7 .6-5.3 4.7L18.3 22 12 18l-6.3 4 1.6-7.7L2 9.6 9 9z"/></svg><svg viewBox="0 0 24 24"><path fill="#f5b800" d="m12 2 3 7 7 .6-5.3 4.7L18.3 22 12 18l-6.3 4 1.6-7.7L2 9.6 9 9z"/></svg><svg viewBox="0 0 24 24"><path fill="#f5b800" d="m12 2 3 7 7 .6-5.3 4.7L18.3 22 12 18l-6.3 4 1.6-7.7L2 9.6 9 9z"/></svg><svg viewBox="0 0 24 24"><path fill="#f5b800" d="m12 2 3 7 7 .6-5.3 4.7L18.3 22 12 18l-6.3 4 1.6-7.7L2 9.6 9 9z"/></svg><svg viewBox="0 0 24 24"><path fill="#f5b800" d="m12 2 3 7 7 .6-5.3 4.7L18.3 22 12 18l-6.3 4 1.6-7.7L2 9.6 9 9z"/></svg></div>
      <blockquote>"Our students love how easy it is to book and reschedule lessons with the AI voice agent. It's like having a receptionist who never sleeps or takes breaks!"</blockquote>
      <div class="author"><div class="author-av" style="background:#e0ebfb;color:#3f6fe0">OC</div><div><div class="author-name">Owen Castillo</div><div class="author-role">Director, Metro Road Academy</div></div></div>
    </article>
    <footer class="footer">
      <div class="brand"><span class="brand-dot"></span>LanePilot.AI</div>
      <p class="footer-desc">Transforming driving schools with AI-powered voice agents that never sleep.</p>
      <div class="socials"><span></span><span></span><span></span></div>
      <div class="f-col" style="left:486px"><h4>Product</h4><ul><li>Features</li><li>Pricing</li><li>Case Studies</li><li>Reviews</li></ul></div>
      <div class="f-col" style="left:926px"><h4>Resources</h4><ul><li>Documentation</li><li>Help Center</li><li>Blog</li><li>API</li></ul></div>
      <div class="f-col" style="left:1366px"><h4>Company</h4><ul><li>About Us</li><li>Careers</li><li>Contact</li><li>Privacy Policy</li></ul></div>
      <div class="footer-rule"></div>
    </footer>
  </section>
</div>
</body>
</html>
```